Offshore Energy Projects Management Consultancy needs a business card design

Logo available. We provide teams to deliver engineering consultancy, project management and delivery teams mainly in the offshore renewables sector. The company is all about bringing the right people to a project to deliver the scope.

The business card will be used for all staff.

The business card should be quite simple, vibrant and uncluttered but convey experience, enthusiasm and integration.

Target Market(s)

Energy Project Developers and Tier 1 construction companies

Contact Information for Business Card

Logo should be on the back of the card. I'm happy for the designer to play with the colour of the logo and background colour.

Front of the card should convey all the must have information in a clear and professional manner but without being overly traditional.

Colors

Designer to choose colors to be used in the design.

Requirements
Must have
• Land Line Tel Number, Mobile Tel Number, Email, business address, web address.

```html
<!DOCTYPE html>
<html lang="en">
<head>
<meta charset="utf-8">
<title>Tidewell Project Partners – Business Card</title>
<link href="https://fonts.googleapis.com/css2?family=Roboto:wght@400;700&display=swap" rel="stylesheet">
<style>
  :root{
    --stage:#e9eaec;
    --brand-blue:#1277c0;
    --accent-blue:#22a0df;
    --ink-grey:#6d6e71;
    --paper:#ffffff;
  }
  *{box-sizing:border-box;margin:0;padding:0}
  html,body{width:1200px;height:900px;overflow:hidden}
  body{background:var(--stage);font-family:'Roboto',Arial,sans-serif;position:relative}

  .card{position:absolute;width:620px;height:354px;box-shadow:0 6px 18px rgba(0,0,0,.12)}

  /* back of card */
  .card-back{left:60px;top:70px;background:var(--brand-blue);display:flex;align-items:center;justify-content:center}
  .back-logo{display:flex;align-items:center;gap:16px;color:var(--paper)}
  .logo-dot{width:22px;height:22px;border-radius:50%;background:var(--paper)}
  .logo-name{font-weight:700;font-size:34px;letter-spacing:.5px;line-height:1.1;text-transform:uppercase}

  /* front of card */
  .card-front{left:520px;top:470px;background:var(--paper);overflow:hidden}
  .front-logo{position:absolute;left:36px;top:46px;display:flex;align-items:center;gap:10px;color:var(--brand-blue)}
  .front-logo .logo-dot{width:14px;height:14px;background:var(--brand-blue)}
  .front-logo .logo-name{font-size:22px}

  .divider{position:absolute;left:36px;right:36px;top:150px;height:2px;background:var(--brand-blue)}

  .holder{position:absolute;right:36px;top:112px;display:flex;align-items:baseline;gap:14px}
  .holder-name{color:var(--accent-blue);font-weight:700;font-size:21px}
  .holder-role{color:var(--ink-grey);font-size:17px}

  .address{position:absolute;left:36px;top:168px;color:var(--ink-grey);font-size:15px;line-height:1.3}
  .contacts{position:absolute;left:44px;top:218px;list-style:none;color:var(--ink-grey);font-size:15px;line-height:1.3}
  .contacts li{display:flex;align-items:center;gap:10px;margin-bottom:2px}
  .contacts svg{width:13px;height:13px;fill:var(--brand-blue);flex:none}

  .base-band{position:absolute;left:0;right:0;bottom:0;height:12px;background:var(--brand-blue)}
</style>
</head>
<body>

<section class="card card-back" aria-label="Card back">
  <div class="back-logo">
    <span class="logo-dot"></span>
    <span class="logo-name">Tidewell<br>Project Partners</span>
  </div>
</section>

<section class="card card-front" aria-label="Card front">
  <div class="front-logo">
    <span class="logo-dot"></span>
    <span class="logo-name">Tidewell<br>Project Partners</span>
  </div>

  <div class="holder">
    <span class="holder-name">Selma Darrow</span>
    <span class="holder-role">CEO</span>
  </div>

  <div class="divider"></div>

  <p class="address">18 Harbour Row 4 B.L.K.<br>Portmere, Eastland</p>

  <ul class="contacts">
    <li>
      <svg viewBox="0 0 16 16" aria-hidden="true"><path d="M3.6 1.2l2.4 2.6-1.3 1.7c.9 2 2.5 3.6 4.6 4.6l1.7-1.3 2.6 2.4-1.3 2.6C6.6 13.4 2.6 9.4 1 3.9z"/></svg>
      +00 123 456 7890
    </li>
    <li>
      <svg viewBox="0 0 16 16" aria-hidden="true"><path d="M4.5 0h7A1.5 1.5 0 0113 1.5v13a1.5 1.5 0 01-1.5 1.5h-7A1.5 1.5 0 013 14.5v-13A1.5 1.5 0 014.5 0zM5 2v10h6V2zm3 11a1 1 0 100 2 1 1 0 000-2z"/></svg>
      +00 123 456 7891
    </li>
    <li>
      <svg viewBox="0 0 16 16" aria-hidden="true"><path d="M1 3h14v10H1zm1.5 1.5v.3L8 9l5.5-4.2v-.3zm0 2.2v4.8h11V6.7L8 10.9z"/></svg>
      info@tidewellpartners.com
    </li>
    <li>
      <svg viewBox="0 0 16 16" aria-hidden="true"><path d="M8 0a8 8 0 110 16A8 8 0 018 0zm0 1.5c-.9 0-2 1.9-2.3 5.5h4.6C10 3.4 8.9 1.5 8 1.5zM1.6 9a6.5 6.5 0 004.1 5.1C5 12.8 4.4 11 4.3 9zm8.7 5.1A6.5 6.5 0 0014.4 9h-2.7c-.1 2-.7 3.8-1.4 5.1zM1.6 7h2.7c.1-2 .7-3.8 1.4-5.1A6.5 6.5 0 001.6 7zm10.1 0h2.7a6.5 6.5 0 00-4.1-5.1c.7 1.3 1.3 3.1 1.4 5.1zM5.7 9c.3 3.6 1.4 5.5 2.3 5.5s2-1.9 2.3-5.5z"/></svg>
      www.tidewellpartners.com
    </li>
  </ul>

  <div class="base-band"></div>
</section>

</body>
</html>
```